Food Safety Consultancy Flyer Design

We need a flyer design for a new company called KLS Training. New food safety regulations are coming into effect for all food operators in March 2016. My company provides training and resources to support food operators during the transition onto the new Kitchen Ledger Scheme. For the designs we would like to see any of the colours used from the logo which is attached. The flyer will be letting operators know that there are new regulations and we are here to help. Our company offers three packages: 1. Videos (training videos) 2. Webinars and Workshop 3. One-on-one mentoring. Our websites main colour used is the green colour from the logo.
Food service operators: cafes, restaurants etc.
Hospitality

```html
<!DOCTYPE html>
<html lang="en">
<head>
<meta charset="utf-8">
<title>KLS Training – Food Act 2014 Flyer</title>
<link rel="stylesheet" href="https://fonts.googleapis.com/css2?family=Montserrat:wght@400;500;600;800&family=Open+Sans:ital,wght@0,400;0,600;1,400&display=swap">
<style>
  :root {
    --stage: #8a8a8a;
    --paper: #ffffff;
    --swoosh-light: #f4f4f5;
    --swoosh-dark: #dcdde0;
    --ink: #2b2b2b;
    --rule: #d8d8d8;
    --title-blue: #1f6fb8;
    --alert-red: #e8383f;
    --tile-orange: #f6ab2f;
    --tile-green: #3cb44a;
    --tile-blue: #1f70b8;
    --tile-red: #f1414c;
    --chef-white: #f3f3f3;
    --chef-shade: #d9d9d9;
    --logo-green: #3cb44a;
  }
  * { box-sizing: border-box; margin: 0; padding: 0; }
  html, body { width: 1200px; height: 799px; overflow: hidden; }
  body {
    background: var(--stage);
    position: relative;
    font-family: "Open Sans", Arial, sans-serif;
    color: var(--ink);
  }

  /* shared page */
  .page {
    position: absolute;
    top: 31px;
    width: 520px;
    height: 736px;
    background: var(--paper);
    overflow: hidden;
    box-shadow: 0 6px 18px rgba(0,0,0,0.25);
  }
  .page--front { left: 55px; }
  .page--back  { left: 625px; }
  .page__swoosh {
    position: absolute;
    left: 0;
    width: 520px;
    height: 300px;
  }
  .page--front .page__swoosh { top: 200px; }
  .page--back  .page__swoosh { top: 400px; }

  /* front */
  .flyer__heading {
    position: absolute;
    top: 42px;
    left: 0;
    width: 100%;
    text-align: center;
    font-family: "Montserrat", Arial, sans-serif;
  }
  .flyer__title { font-weight: 500; font-size: 34px; color: var(--title-blue); }
  .flyer__date { font-weight: 500; font-size: 13.5px; color: var(--alert-red); }

  .chef-grid {
    position: absolute;
    top: 122px;
    left: 88px;
    display: grid;
    grid-template-columns: 165px 165px;
    gap: 14px;
  }
  .chef-tile { height: 160px; position: relative; }
  .chef-tile--orange { background: var(--tile-orange); }
  .chef-tile--green  { background: var(--tile-green); }
  .chef-tile--blue   { background: var(--tile-blue); }
  .chef-tile--red    { background: var(--tile-red); }
  .chef-figure {
    position: absolute;
    background: linear-gradient(var(--chef-white), var(--chef-shade));
    border-radius: 22px 22px 4px 4px;
  }
  .chef-tile .chef-figure { left: 55px; top: 16px; width: 55px; height: 144px; }

  .flyer__intro {
    position: absolute;
    top: 483px;
    left: 30px;
    width: 460px;
    font-size: 11.5px;
    line-height: 1.35;
    text-align: center;
  }
  .flyer__lower {
    position: absolute;
    top: 530px;
    left: 0;
    width: 100%;
    height: 206px;
    border-top: 1px solid #efefef;
  }
  .knowledge {
    position: absolute;
    top: 22px;
    left: 64px;
    font-size: 9px;
    font-style: italic;
    line-height: 1.5;
  }
  .knowledge__tagline { margin-bottom: 10px; }
  .knowledge__list { list-style: none; margin-top: 2px; }
  .knowledge__list li { font-style: normal; font-weight: 600; font-size: 8.5px; }
  .knowledge__list li::before { content: "• "; }
  .brand {
    position: absolute;
    top: 80px;
    left: 290px;
    display: flex;
    align-items: center;
    gap: 10px;
    font-family: "Montserrat", Arial, sans-serif;
    font-weight: 600;
    font-size: 22px;
    color: var(--logo-green);
  }
  .brand__dot { width: 24px; height: 24px; border-radius: 50%; background: var(--logo-green); }
  .flyer__closing {
    position: absolute;
    bottom: 22px;
    right: 30px;
    font-size: 9px;
    font-weight: 600;
    color: var(--title-blue);
  }

  /* back */
  .back__headline {
    position: absolute;
    top: 44px;
    left: 190px;
    width: 290px;
    font-family: "Montserrat", Arial, sans-serif;
    font-weight: 800;
    font-size: 21px;
    line-height: 1.15;
    color: #111;
  }
  .back__title {
    position: absolute;
    top: 148px;
    left: 205px;
    font-family: "Montserrat", Arial, sans-serif;
    font-weight: 500;
    font-size: 24px;
    color: var(--title-blue);
  }
  .packages {
    position: absolute;
    top: 150px;
    left: 40px;
    width: 390px;
    height: 250px;
    display: grid;
    grid-template-columns: repeat(3, 1fr);
    border: 1px solid var(--rule);
    background: var(--paper);
  }
  .package { position: relative; border-right: 1px solid var(--rule); }
  .package:last-child { border-right: 0; }
  .package:nth-child(2) { padding-top: 42px; }
  .package:nth-child(3) { padding-top: 84px; }
  .package__band {
    height: 30px;
    display: flex;
    align-items: center;
    justify-content: center;
  }
  .package--orange .package__band { background: var(--tile-orange); }
  .package--green  .package__band { background: var(--tile-green); }
  .package--red    .package__band { background: var(--tile-red); }
  .package__num {
    width: 20px;
    height: 20px;
    border-radius: 50%;
    background: var(--paper);
    border: 1px solid #333;
    font-size: 11px;
    font-weight: 600;
    text-align: center;
    line-height: 18px;
  }
  .package__name {
    font-size: 9.5px;
    font-weight: 600;
    padding: 7px 10px;
    border-bottom: 1px solid var(--rule);
  }
  .package__text {
    font-size: 9px;
    line-height: 1.45;
    padding: 7px 10px;
  }
  .page--back .chef-figure--small { left: 395px; top: 195px; width: 80px; height: 150px; }
  .page--back .chef-figure--large { left: 110px; top: 420px; width: 150px; height: 300px; border-radius: 60px 60px 6px 6px; }
</style>
</head>
<body>
  <!-- Front side -->
  <article class="page page--front">
    <svg class="page__swoosh" viewBox="0 0 520 300" role="img" aria-label="Soft grey decorative swoosh background">
      <defs>
        <linearGradient id="swoosh-front" x1="0" y1="0" x2="1" y2="1">
          <stop offset="0" stop-color="#ffffff"/>
          <stop offset="0.5" stop-color="#e9eaec"/>
          <stop offset="1" stop-color="#ffffff"/>
        </linearGradient>
      </defs>
      <rect width="520" height="300" fill="url(#swoosh-front)"/>
    </svg>

    <header class="flyer__heading">
      <h1 class="flyer__title">The Food Act 2014</h1>
      <p class="flyer__date">comes into force on 1 March 2016.</p>
    </header>

    <section class="chef-grid">
      <div class="chef-tile chef-tile--orange" role="img" aria-label="Illustrated chef holding broccoli and a knife on orange">
        <span class="chef-figure"></span>
      </div>
      <div class="chef-tile chef-tile--green" role="img" aria-label="Illustrated chef holding a spatula and fork on green">
        <span class="chef-figure"></span>
      </div>
      <div class="chef-tile chef-tile--blue" role="img" aria-label="Illustrated chef holding a ladle and a pot on blue">
        <span class="chef-figure"></span>
      </div>
      <div class="chef-tile chef-tile--red" role="img" aria-label="Illustrated chef carrying a serving cloche on red">
        <span class="chef-figure"></span>
      </div>
    </section>

    <p class="flyer__intro">Food service and food retailers will be on Kitchen Ledger Schemes – documentation of processes and risk management to produce safe and suitable food.</p>

    <section class="flyer__lower">
      <div class="knowledge">
        <p class="knowledge__tagline">KLS Training – Your reputation is our business</p>
        <p>With up-to-date knowledge on:</p>
        <ul class="knowledge__list">
          <li>The Food Act 2014</li>
          <li>Kitchen Ledger Scheme requirements</li>
          <li>Verification expectations</li>
          <li>New Food Grading system</li>
          <li>New Fees</li>
        </ul>
      </div>
      <div class="brand">
        <span class="brand__dot"></span>
        <span class="brand__name">KLS Training</span>
      </div>
    </section>

    <p class="flyer__closing">Let us help you transition and understand all there is to know.</p>
  </article>

  <!-- Back side -->
  <article class="page page--back">
    <svg class="page__swoosh" viewBox="0 0 520 300" role="img" aria-label="Soft grey decorative swoosh background">
      <defs>
        <linearGradient id="swoosh-back" x1="0" y1="0" x2="1" y2="1">
          <stop offset="0" stop-color="#ffffff"/>
          <stop offset="0.5" stop-color="#e9eaec"/>
          <stop offset="1" stop-color="#ffffff"/>
        </linearGradient>
      </defs>
      <rect width="520" height="300" fill="url(#swoosh-back)"/>
    </svg>

    <h2 class="back__headline">Let us help you transition and understand all there is to know.</h2>

    <span class="chef-figure chef-figure--small" role="img" aria-label="Illustrated chef holding broccoli and a knife"></span>
    <span class="chef-figure chef-figure--large" role="img" aria-label="Large illustrated chef carrying a serving cloche"></span>

    <section class="packages" aria-label="Our Packages">
      <div class="package package--orange">
        <div class="package__band"><span class="package__num">1</span></div>
        <p class="package__name">Videos</p>
        <p class="package__text">Animated training videos of the KLS, 6 month subscription. Ten modules included.</p>
      </div>
      <div class="package package--green">
        <div class="package__band"><span class="package__num">2</span></div>
        <p class="package__name">Webinars/Workshops</p>
        <p class="package__text">A range of webinars at set times for the industry. Live training with a subscription; a recorded library is included.</p>
      </div>
      <div class="package package--red">
        <div class="package__band"><span class="package__num">3</span></div>
        <p class="package__name">One-to-one mentoring</p>
        <p class="package__text">We come to you and go through the KLS page-by-page.</p>
      </div>
    </section>

    <h3 class="back__title">Our Packages</h3>
  </article>
</body>
</html>
```